Design for a Note buying company that attracts landlords and seller financed notes

I need a card designed. I want a simple clean front with my logo and contact info. On the back I want some big and bold words to get a message across.

Our Company buys Notes (mortgages) and we want to convey the sense of financial security. Our number one market that we pursue is tired landlords.

If you want to understand our business you can visit our website. www.lakeviewpaperfund.com

Do not use any Clip Art in the design, it will not be accepted. I want a custom designed card not something I could throw together myself. Simple clean and drive the message home.

Target Market(s)

Landlords, seller financed note holders

Industry/Entity Type

Mortgage

Contact Information for Business Card

Simple clean and bold. I need to grab the attention of the customer. It should convey a professional touch.

Font styles to use
Sans Serif

Colors
ec2229
ffffff

Requirements
Must have
• Clean front with logo and contact information
Front colors should match logo

Back should be bold and grab attention. Back colors are open to ideas
Nice to have
• The Back May use the phrase "No more Repairs, No more Late Rent" "More Freedom, More Income"

I'm open to other ideas about grabbing a landlords attention

I'm open to a square card design
I like cards with round corners as well
Should not have
• any clip art! must be custom designs.

```html
<!DOCTYPE html>
<html lang="en">
<head>
<meta charset="utf-8">
<title>Lakeview Paper Fund – Business Card</title>
<link href="https://fonts.googleapis.com/css2?family=Lato:ital,wght@0,400;0,700;0,900;1,700;1,900&display=swap" rel="stylesheet">
<style>
  :root {
    --brand-red: #ec2229;
    --paper: #ffffff;
    --ink: #111111;
    --backdrop: #f1f1f1;
    --edge: #d6d6d6;
  }
  * { box-sizing: border-box; margin: 0; padding: 0; }
  html, body {
    width: 1200px; height: 1200px; overflow: hidden;
    background: var(--backdrop);
    font-family: "Lato", sans-serif;
  }
  .stage { position: relative; width: 1200px; height: 1200px; }
  .card {
    position: absolute; left: 378px; width: 444px; height: 444px;
    border-radius: 56px; text-align: center;
  }
  .card-front { top: 132px; background: var(--paper); border: 1px solid var(--edge); }
  .card-back { top: 624px; background: var(--brand-red); color: var(--paper); }

  .tagline {
    position: absolute; top: 72px; left: 0; right: 0;
    font-size: 14px; font-weight: 700; letter-spacing: 6px; color: var(--ink);
  }
  .wordmark {
    position: absolute; top: 108px; left: 0; right: 0;
    font-weight: 900; color: var(--ink); line-height: 1;
  }
  .wordmark-main { display: block; font-size: 58px; letter-spacing: 1px; }
  .wordmark-sub { display: block; font-size: 26px; letter-spacing: 9px; margin-top: 28px; }

  .person-name {
    position: absolute; top: 264px; left: 0; right: 0;
    font-size: 25px; font-weight: 700; color: var(--brand-red);
  }
  .person-company {
    position: absolute; top: 290px; left: 0; right: 0;
    font-size: 19px; font-weight: 400; color: var(--ink);
  }
  .address {
    position: absolute; top: 345px; left: 0; right: 0;
    font-size: 17px; line-height: 19px; color: var(--ink);
  }
  .contact-row {
    position: absolute; top: 401px; left: 0; right: 0;
    display: flex; justify-content: center; align-items: center; gap: 9px;
    font-size: 17px; color: var(--ink);
  }
  .contact-item { display: flex; align-items: center; gap: 6px; }
  .contact-icon { width: 18px; height: 18px; }

  .slogan {
    position: absolute; top: 86px; left: 0; right: 0;
    font-size: 24px; font-weight: 900; font-style: italic; line-height: 34px;
    letter-spacing: -0.3px;
  }
  .back-wordmark {
    position: absolute; top: 232px; left: 0; right: 0;
    font-weight: 900; line-height: 1;
  }
  .back-wordmark-main { display: block; font-size: 54px; }
  .back-wordmark-sub { display: block; font-size: 24px; letter-spacing: 9px; margin-top: 14px; }
</style>
</head>
<body>
<main class="stage">
  <section class="card card-front">
    <p class="tagline">WE HELP OWNERS THRIVE!</p>
    <h1 class="wordmark">
      <span class="wordmark-main">LAKEVIEW</span>
      <span class="wordmark-sub">PAPER FUND</span>
    </h1>
    <p class="person-name">Dana Whitfield</p>
    <p class="person-company">Lakeview Capital Partners</p>
    <p class="address">P.O.Box 112<br>Millbrook, Kansas 67099</p>
    <div class="contact-row">
      <span class="contact-item">
        <svg class="contact-icon" viewBox="0 0 20 20" aria-hidden="true">
          <circle cx="10" cy="10" r="10" fill="#ec2229"/>
          <path d="M6.2 5.2l2 0 1 2.6-1.3 1c.6 1.3 1.5 2.2 2.8 2.8l1-1.3 2.6 1v2c0 .6-.5 1-1 1C9 14.2 5.8 11 5.2 6.2c0-.5.4-1 1-1z" fill="#fff"/>
        </svg>
        316-555-0142
      </span>
      <span class="contact-item">
        <svg class="contact-icon" viewBox="0 0 20 20" aria-hidden="true">
          <circle cx="10" cy="10" r="10" fill="#ec2229"/>
          <rect x="5" y="6.5" width="10" height="7" fill="none" stroke="#fff" stroke-width="1.2"/>
          <path d="M5 6.5l5 4 5-4" fill="none" stroke="#fff" stroke-width="1.2"/>
        </svg>
        info@lakeviewpaperfund.com
      </span>
    </div>
  </section>

  <section class="card card-back">
    <p class="slogan">"No more Repairs, No more Late Rent"<br>"More Freedom, More Income"</p>
    <p class="back-wordmark">
      <span class="back-wordmark-main">LAKEVIEW</span>
      <span class="back-wordmark-sub">PAPER FUND</span>
    </p>
  </section>
</main>
</body>
</html>
```